Redesign of Business Card to look more professional and stand out

Business card design. You can lean more about our company by going to dlmfabworks.example. Raised letters would be nice. Company name & Address
DL&M
418 Wrenfield Crest Drive, Suite 140
Birmingham, AL 35999

You can use my name and title: Glenn Marlowe
Business Development Manager

Target Market(s)

Heavy Industrial market, i.e. utilities, chemical plants, paper mills, construction companies

Industry/Entity Type

Construction

Contact Information for Business Card

We provide Project Management & Project Support Services

Font styles to use
Serif

Requirements
Must have
• Company name & Address
• DL&M
• 418 Wrenfield Crest Drive, Suite 140
• Birmingham, AL 35999
Nice to have
• ideas for the back of the card
Should not have
• no crazy colors. needs to look professional and standout.

```html
<!DOCTYPE html>
<html lang="en">
<head>
<meta charset="utf-8">
<title>DL&amp;M Business Card</title>
<link rel="stylesheet" href="https://fonts.googleapis.com/css2?family=Open+Sans:wght@400;600;800&family=Titillium+Web:wght@600&display=swap">
<style>
  :root {
    --backdrop: #4a3d38;
    --card-black: #1c1c1d;
    --card-black-mark: #2b2b2d;
    --card-blue: #1d3567;
    --silver: #c9ccd1;
    --ink-light: #ffffff;
    --ink-soft: #dfe5f0;
    --divider: rgba(255,255,255,0.55);
  }
  * { margin: 0; padding: 0; box-sizing: border-box; }
  html, body { width: 1200px; height: 716px; overflow: hidden; }
  body {
    background: var(--backdrop);
    font-family: "Open Sans", sans-serif;
    position: relative;
  }
  .card {
    position: absolute;
    top: 208px;
    width: 520px;
    height: 300px;
    border-radius: 3px;
    box-shadow: 0 10px 24px rgba(0,0,0,0.45);
  }
  .card-back {
    left: 50px;
    background: var(--card-black);
  }
  .card-back .back-mark {
    position: absolute;
    left: 0; right: 0; top: 88px;
    text-align: center;
    font-family: "Open Sans", sans-serif;
    font-weight: 800;
    font-size: 96px;
    letter-spacing: 2px;
    color: var(--card-black-mark);
  }
  .card-back .back-url {
    position: absolute;
    left: 96px; bottom: 46px;
    font-size: 14px;
    color: var(--ink-light);
  }
  .card-front {
    left: 630px;
    background: var(--card-blue);
  }
  .front-mark {
    position: absolute;
    left: 38px; top: 104px;
    font-weight: 800;
    font-size: 62px;
    letter-spacing: 1px;
    color: var(--silver);
  }
  .front-divider {
    position: absolute;
    left: 242px; top: 40px;
    width: 1px; height: 220px;
    background: var(--divider);
  }
  .contact-block {
    position: absolute;
    left: 266px; top: 60px;
    color: var(--ink-light);
  }
  .person-name {
    font-family: "Titillium Web", sans-serif;
    font-weight: 600;
    font-size: 19px;
    line-height: 1.1;
  }
  .person-title {
    font-size: 12.5px;
    color: var(--ink-soft);
    margin-bottom: 22px;
  }
  .address { font-size: 13.5px; line-height: 1.35; margin-bottom: 4px; }
  .contact-line {
    display: flex; align-items: center; gap: 9px;
    font-size: 13.5px; line-height: 1.5;
  }
  .contact-line svg { width: 13px; height: 13px; flex: none; }
</style>
</head>
<body>
  <section class="card card-back" aria-label="Card back">
    <div class="back-mark">DL&amp;M</div>
    <div class="back-url">www.dlmfabworks.example</div>
  </section>

  <section class="card card-front" aria-label="Card front">
    <div class="front-mark">DL&amp;M</div>
    <div class="front-divider"></div>
    <div class="contact-block">
      <div class="person-name">Glenn Marlowe</div>
      <div class="person-title">Managing Director</div>
      <div class="address">418 Wrenfield Crest Drive, Suite 140<br>Birmingham, AL 35999</div>
      <div class="contact-line">
        <svg viewBox="0 0 16 16" aria-hidden="true"><path fill="#fff" d="M3 2h3l1 4-2 1c1 2 2 3 4 4l1-2 4 1v3c0 1-1 1-1 1C7 14 2 9 2 3c0 0 0-1 1-1z"/></svg>
        <span>205.555.0148</span>
      </div>
      <div class="contact-line">
        <svg viewBox="0 0 16 16" aria-hidden="true"><rect x="1" y="3" width="14" height="10" fill="#fff"/><path d="M1 3l7 6 7-6" fill="none" stroke="#1d3567" stroke-width="1.3"/></svg>
        <span>gmarlowe@dlmfabworks.example</span>
      </div>
      <div class="contact-line">
        <svg viewBox="0 0 16 16" aria-hidden="true"><circle cx="8" cy="8" r="6.5" fill="none" stroke="#fff" stroke-width="1.4"/><ellipse cx="8" cy="8" rx="2.8" ry="6.5" fill="none" stroke="#fff" stroke-width="1.1"/><path d="M1.5 8h13" stroke="#fff" stroke-width="1.1"/></svg>
        <span>www.dlmfabworks.example</span>
      </div>
    </div>
  </section>
</body>
</html>
```